Box for Colorado based custom buckle and belt company

We are looking to design a box to be used to hold belts that will be delivered through Tolvaro's QSP program. It should have a rustic/western feel (potentially as basic as simulated mountains) and include our company's name (R&K Buckles), website (www.randkbuckles.com). There needs to be a place to attach a sticker containing a SKU on the back or side of the box.

Target Market(s)

Primary customers will be men. Our products are on the more expensive side (e.g., $100-350 for a belt).

Most customers will consider themselves to be "weekend cowboys." Someone who enjoys the western ideas, but does not live then 7 days a week.

Industry/Entity Type

Clothing

Font styles to use
Serif

Requirements
Must have
• -Company Name: R&K Buckles
• -Website: www.randkbuckles.com
• -Contact info: pat@randkbuckles.com and (800) 647-1928
Should not have
• Overly complicated. Would prefer clean and simple.

```html
<!DOCTYPE html>
<html lang="en">
<head>
<meta charset="utf-8">
<title>R&amp;K Buckles – Mailer Box Dieline</title>
<link rel="stylesheet" href="https://fonts.googleapis.com/css2?family=EB+Garamond:ital,wght@0,400;1,400&display=swap">
<style>
  :root {
    --board: #f3efe0;
    --swatch-cream: #f2e8cf;
    --brown: #8c7553;
    --ink: #111111;
    --cut: #a3dccd;
    --cut-inner: #a9d6e6;
    --fold: #f0a79c;
    --page: #ffffff;
  }
  html, body {
    margin: 0;
    width: 1200px;
    height: 1091px;
    overflow: hidden;
    background: var(--page);
  }
  .dieline { display: block; }
  .panel { fill: var(--board); stroke: var(--cut); stroke-width: 1; }
  .inner-cut { fill: none; stroke: var(--cut-inner); stroke-width: 1; }
  .fold { stroke: var(--fold); stroke-width: 1; fill: none; }
  .slot { fill: var(--board); stroke: var(--cut-inner); stroke-width: 1; }
  .company-name, .side-name, .side-url, .back-copy, .sku-label {
    font-family: "EB Garamond", Georgia, serif;
    font-weight: 400;
    fill: var(--ink);
  }
  .company-name { font-size: 30px; letter-spacing: 4px; }
  .company-name-flap { font-size: 17px; letter-spacing: 3px; }
  .side-name { font-size: 13px; letter-spacing: 2.5px; }
  .side-url { font-size: 11.5px; }
  .back-copy { font-size: 10.5px; }
  .back-copy .italic { font-style: italic; }
  .sku-box { fill: #ffffff; }
  .sku-label { font-size: 9.5px; }
  .mountain-art { fill: var(--brown); opacity: 0.35; }
  .swatch-cream { fill: var(--swatch-cream); }
  .swatch-brown { fill: var(--brown); }
  .swatch-black { fill: var(--ink); }
</style>
</head>
<body>
<svg class="dieline" width="1200" height="1091" viewBox="0 0 1200 1091" xmlns="http://www.w3.org/2000/svg">

  <!-- top lid dust flap -->
  <rect class="panel" x="414" y="32" width="372" height="124"/>
  <line class="fold" x1="428" y1="46" x2="428" y2="156"/>
  <line class="fold" x1="772" y1="46" x2="772" y2="156"/>
  <line class="fold" x1="428" y1="156" x2="772" y2="156"/>

  <!-- top corner flaps -->
  <path class="panel" d="M264 50 Q264 46 268 46 L414 46 L414 142 L300 142 L264 128 Z"/>
  <path class="panel" d="M936 50 Q936 46 932 46 L786 46 L786 142 L900 142 L936 128 Z"/>

  <!-- outer side flaps -->
  <rect class="panel" x="170" y="146" width="136" height="354" rx="20"/>
  <rect class="inner-cut" x="184" y="158" width="112" height="330" rx="10"/>
  <rect class="panel" x="894" y="146" width="136" height="354" rx="20"/>
  <rect class="inner-cut" x="904" y="158" width="112" height="330" rx="10"/>

  <!-- side walls and base -->
  <rect class="panel" x="296" y="154" width="608" height="336"/>
  <line class="fold" x1="306" y1="154" x2="306" y2="490"/>
  <line class="fold" x1="420" y1="154" x2="420" y2="490"/>
  <line class="fold" x1="780" y1="154" x2="780" y2="490"/>
  <line class="fold" x1="894" y1="154" x2="894" y2="490"/>

  <!-- hand slots -->
  <rect class="slot" x="419" y="280" width="14" height="84" rx="7"/>
  <rect class="slot" x="767" y="280" width="14" height="84" rx="7"/>

  <!-- left side wall -->
  <g transform="translate(352 320) rotate(90)">
    <text class="side-name" text-anchor="middle" y="4">R&amp;K BUCKLES</text>
  </g>
  <g transform="translate(383 320) rotate(-90)">
    <text class="side-url" text-anchor="middle" y="4">randkbuckles.com</text>
  </g>

  <!-- right side wall -->
  <g transform="translate(844 322) rotate(90)">
    <text class="side-name" text-anchor="middle" y="4">R&amp;K BUCKLES</text>
  </g>
  <g transform="translate(816 326) rotate(90)">
    <text class="side-url" text-anchor="middle" y="4">randkbuckles.com</text>
  </g>

  <!-- lower corner flaps -->
  <path class="panel" d="M258 502 L296 500 L410 500 L410 598 L262 598 Q258 598 258 594 Z"/>
  <path class="panel" d="M942 502 L904 500 L790 500 L790 598 L938 598 Q942 598 942 594 Z"/>
  <rect class="inner-cut" x="272" y="504" width="138" height="90" rx="2"/>
  <rect class="inner-cut" x="790" y="504" width="138" height="90" rx="2"/>

  <!-- back wall with contact details -->
  <rect class="panel" x="422" y="488" width="356" height="110"/>
  <line class="fold" x1="422" y1="488" x2="778" y2="488"/>
  <line class="fold" x1="422" y1="598" x2="778" y2="598"/>
  <g transform="translate(656 543) rotate(180)">
    <text class="back-copy" text-anchor="middle" y="-36">R&amp;K Buckles</text>
    <text class="back-copy" text-anchor="middle" y="-22">randkbuckles.com</text>
    <text class="back-copy" text-anchor="middle" y="6"><tspan class="italic">Any Questions?  Please contact us at:</tspan></text>
    <text class="back-copy" text-anchor="middle" y="20">pat@randkbuckles.com</text>
    <text class="back-copy" text-anchor="middle" y="34"><tspan class="italic">or by phone at:</tspan>  (800) 647-1928</text>
  </g>
  <rect class="sku-box" x="455" y="502" width="83" height="80"/>
  <g transform="translate(496 542) rotate(180)">
    <text class="sku-label" text-anchor="middle" y="-10">Bar Code</text>
    <text class="sku-label" text-anchor="middle" y="1">&amp; SKU #</text>
    <text class="sku-label" text-anchor="middle" y="12">Area</text>
  </g>

  <!-- lid -->
  <path class="panel" d="M352 600 L848 600 Q890 604 890 650 L890 884 Q890 916 868 922 L766 932 L434 932 L332 922 Q310 916 310 884 L310 650 Q310 604 352 600 Z"/>
  <path class="inner-cut" d="M434 604 L358 614 Q326 618 326 652 L326 880 Q326 914 360 918 L434 928"/>
  <path class="inner-cut" d="M766 604 L842 614 Q874 618 874 652 L874 880 Q874 914 840 918 L766 928"/>
  <line class="fold" x1="434" y1="600" x2="434" y2="932"/>
  <line class="fold" x1="766" y1="600" x2="766" y2="932"/>
  <line class="fold" x1="434" y1="932" x2="766" y2="932"/>

  <rect class="mountain-art" x="496" y="718" width="206" height="42" role="img" aria-label="Line drawing of a rugged mountain range in brown"/>
  <text class="company-name" x="602" y="806" text-anchor="middle">R&amp;K BUCKLES</text>

  <!-- front tuck flap -->
  <path class="panel" d="M304 950 Q304 934 322 934 L878 934 Q896 934 896 950 L896 994 Q896 1058 830 1058 L370 1058 Q304 1058 304 994 Z"/>
  <path class="inner-cut" d="M318 956 Q318 946 330 946 L424 946 L424 1046 L372 1046 Q318 1046 318 994 Z"/>
  <path class="inner-cut" d="M882 956 Q882 946 870 946 L776 946 L776 1046 L828 1046 Q882 1046 882 994 Z"/>
  <line class="fold" x1="424" y1="934" x2="424" y2="1046"/>
  <line class="fold" x1="776" y1="934" x2="776" y2="1046"/>
  <text class="company-name company-name-flap" x="602" y="1000" text-anchor="middle">R&amp;K BUCKLES</text>

  <!-- colour palette -->
  <rect class="swatch-cream" x="49" y="957" width="54" height="54"/>
  <rect class="swatch-brown" x="113" y="957" width="54" height="54"/>
  <rect class="swatch-black" x="177" y="957" width="54" height="54"/>
</svg>
</body>
</html>
```